Webdesign for Property Renting Business

We need a professional and slim design for a hight quality property renting website which is not overcrowded with too much information and has a clear and easily structure to read. The visitor should get an instant impression what he can do at a glance.

The goal of this contest is to get a design for building a prototype of the website and to attract our client and owner of the site by a good looking prototype and not just a wireframe. Therefore we don't need an HTML-coded design at this early project-stage. We only expect getting a simple bitmap or vector-graphic design.

Actually we don't have a logo. Use a placeholder or feel free to design a simple one by yourself.

Last but not least if you have a good idea just include it in to your design.

Our goal is to get a design for building a prototype of the website and to attract our client by a good looking prototype and not just a wireframe.

Target Market(s)

People who want to spend money to rent a good quality property. Not only the riches. These could be business people and also demanding families as well.

Industry/Entity Type

Building

Colors
85cae6

Requirements
Must have
• We need two sites, a start site and a property-details site. Each site has to include the following points:

1.) start site
- search mask (location, date to choose, quanity of guests)
- show some properties (highlights, special offers etc.)
- show login/register link

2.) property site
- Location in Vorlen Map
- Photos, Description, Amenities, Calendar (available,not available), Contact, Reviews

These are some sites which I like from a design prospective
- http://www.stayquelo.com
- http://www.lodvanta.com/
- http://www.dwellirox.com/
- http://www.plomavi.com

These are some sites which I dislike:
1.) http://www.gallic-estatio.com/guides/france/rent/
2.) http://www.solohomvenu.co.za/property-rentals.htm

We don't need an HTML-coded design at this early project-stage. We only expect getting a simple bitmap or vector-graphic design. Maybe with the PSD-file (or wathever program you use) that we can pick-out some elements for building the prototype.

```html
<!DOCTYPE html>
<html lang="en">
<head>
<meta charset="utf-8">
<title>Nestaro Rent</title>
<link href="https://fonts.googleapis.com/css2?family=Signika:wght@400;600;700&family=Fira+Sans:wght@400;500&display=swap" rel="stylesheet">
<style>
  :root {
    --sky: #29a9e0;
    --sky-dark: #1a86c2;
    --orange: #f7941d;
    --hot: #f26522;
    --lime: #a6ce39;
    --teal: #0aa5b0;
    --ink: #1c1c1c;
    --paper: #ffffff;
    --mist: #e9e9e9;
    --backdrop: #f4f4f4;
    --rule: #9a9a9a;
    --icon: #8c8c8c;
  }
  * { box-sizing: border-box; margin: 0; padding: 0; }
  html, body { width: 1200px; height: 905px; overflow: hidden; }
  body {
    background: var(--backdrop);
    font-family: "Signika", "Fira Sans", sans-serif;
    color: var(--ink);
    position: relative;
  }
  .page {
    position: absolute; left: 123px; top: 0; width: 955px; height: 905px;
    background: var(--mist);
    box-shadow: 0 0 28px rgba(0,0,0,.22);
  }
  .site-header { position: absolute; left: 0; top: 0; width: 955px; height: 113px; background: var(--paper); }
  .brand { position: absolute; left: 32px; top: 31px; display: flex; align-items: center; gap: 10px; }
  .brand-square { width: 50px; height: 50px; background: var(--sky); }
  .brand-name { font-weight: 700; font-size: 38px; line-height: 50px; color: var(--sky); letter-spacing: .3px; }
  .login-btn {
    position: absolute; left: 818px; top: 43px; width: 90px; height: 27px;
    background: linear-gradient(#2c9ee0, var(--sky-dark)); color: #fff;
    border-radius: 4px; font-weight: 600; font-size: 15px;
    display: flex; align-items: center; justify-content: center;
  }
  .register { position: absolute; right: 45px; top: 78px; font-size: 14px; font-weight: 600; }
  .register a { color: var(--sky); text-decoration: none; }

  .hero {
    position: absolute; left: 0; top: 113px; width: 955px; height: 363px;
    background: linear-gradient(180deg, #e4e4e2 0%, #d6d3cf 45%, #a88f78 75%, #7c624a 100%);
  }
  .search-panel {
    position: absolute; left: 183px; top: 94px; width: 590px; height: 136px;
    background: rgba(255,255,255,.55);
  }
  .field {
    position: absolute; background: #fff; border: 2px solid #555; border-radius: 7px;
    font-family: "Fira Sans", sans-serif; color: #444;
    display: flex; align-items: center; justify-content: center;
  }
  .field-location { left: 27px; top: 33px; width: 329px; height: 34px; font-size: 24px; }
  .field-small { top: 82px; height: 33px; font-size: 15px; }
  .field-checkin { left: 28px; width: 76px; }
  .field-checkout { left: 115px; width: 76px; }
  .field-guests { left: 203px; width: 74px; }
  .find-btn {
    position: absolute; left: 421px; top: 52px; width: 122px; height: 35px;
    background: var(--orange); color: #fff; border-radius: 5px;
    font-weight: 600; font-size: 21px;
    display: flex; align-items: center; justify-content: center;
  }
  .accent-band { position: absolute; left: 0; top: 476px; width: 955px; height: 16px; background: var(--sky); }

  .circle {
    position: absolute; width: 112px; height: 112px; border-radius: 50%;
    color: #fff; font-weight: 600; text-align: center; line-height: 1.2;
    display: flex; align-items: center; justify-content: center;
  }
  .circle-hot { left: 44px; top: 583px; background: var(--hot); font-size: 21px; }
  .circle-properties { left: 639px; top: 583px; background: var(--lime); font-size: 17px; }
  .circle-offers { left: 775px; top: 583px; background: var(--teal); font-size: 20px; }
  .divider { position: absolute; left: 171px; top: 539px; width: 2px; height: 200px; background: var(--rule); }
  .promo-slide {
    position: absolute; left: 190px; top: 550px; width: 319px; height: 179px;
    background: linear-gradient(135deg, #7a6352 0%, #b69a80 40%, #3f8f86 70%, #5a4334 100%);
  }
  .slide-arrow { position: absolute; right: 8px; }
  .promo-caption {
    position: absolute; left: 190px; top: 743px; width: 340px;
    font-family: "Fira Sans", sans-serif; font-weight: 500; font-size: 13.5px; line-height: 18px;
  }
  .footer-rule { position: absolute; left: 29px; top: 863px; width: 897px; height: 1px; background: var(--rule); }
  .social { position: absolute; right: 36px; top: 874px; display: flex; gap: 12px; }
  .social span {
    display: flex; align-items: center; gap: 5px;
    font-family: "Fira Sans", sans-serif; font-size: 13px; font-weight: 500; color: var(--icon);
  }
  .social i { width: 16px; height: 16px; background: var(--icon); display: block; }
</style>
</head>
<body>
<div class="page">
  <header class="site-header">
    <div class="brand"><span class="brand-square"></span><span class="brand-name">Nestaro Rent</span></div>
    <div class="login-btn">LOG IN</div>
    <p class="register">Not yet a member? <a href="#">Register Now!</a></p>
  </header>

  <section class="hero" role="img" aria-label="Photo of a bright loft apartment with dining table, wooden chairs and white sofa">
    <form class="search-panel">
      <div class="field field-location">Enter your desired location</div>
      <div class="field field-small field-checkin">Check-In</div>
      <div class="field field-small field-checkout">Check-Out</div>
      <div class="field field-small field-guests">Guests</div>
      <div class="find-btn">FIND IT!</div>
    </form>
  </section>
  <div class="accent-band"></div>

  <div class="circle circle-hot">HOT<br>DEALS</div>
  <div class="divider"></div>
  <div class="promo-slide" role="img" aria-label="Photo of a featured living room with hanging fireplace and teal sofa">
    <svg class="slide-arrow" style="top:70px" width="12" height="16" viewBox="0 0 12 16"><path d="M3 2l6 6-6 6" fill="none" stroke="#fff" stroke-width="2"/></svg>
    <svg class="slide-arrow" style="top:102px" width="12" height="16" viewBox="0 0 12 16"><path d="M9 2L3 8l6 6" fill="none" stroke="#fff" stroke-width="2"/></svg>
  </div>
  <p class="promo-caption">This area is for the descriptions of the promotions shown on each picture above. Book it Now!</p>
  <div class="circle circle-properties">PROPERTIES</div>
  <div class="circle circle-offers">SPECIAL<br>OFFERS</div>

  <div class="footer-rule"></div>
  <div class="social">
    <span><i></i>Plazo</span>
    <span><i></i>Chirpa</span>
    <span><i></i>Snapgrid</span>
  </div>
</div>
</body>
</html>
```